Knee Wraps

brand name is velmo
300g package
collagen product containing bovine collagen peptides
orange packaging color
with turmeric added
ultimate complex for joints flexibility & mobility
ingredients
collagen, turmeric curcumin, vitamin c
a product that takes care of the joints mobility and provides resilience against injuries

similar design to the packaging in the files

Target Market(s)

fitness, health products

Industry/Entity Type

health and fitness

Colors
F0912C
F2A743
F7CA91
FBE8D2
FDF5EE

Requirements
Must have
• very clear message of the advantage of the product which is providing flexible joints, increased mobility, great inflammation response, amazing skin hair bones and nails care
Nice to have
• turmeric design or something that indicates the product containing organic turmeric, orange fresh design, something to makes me feel happy with movement of my body/joints

```html
<!DOCTYPE html>
<html lang="en">
<head>
<meta charset="utf-8">
<title>velmo Collagen Peptides – Label</title>
<link rel="stylesheet" href="https://fonts.googleapis.com/css2?family=Bebas+Neue&family=Oswald:wght@300;400&family=Nunito+Sans:ital,wght@0,400;0,600;0,800;1,600;1,700&display=swap">
<style>
  :root {
    --orange-deep: #d98a1f;
    --orange: #e9a33c;
    --orange-soft: #f2b85c;
    --cream: #fdf5ee;
    --panel: #f4f4f6;
    --ink: #2b2f38;
    --stage: #efe6d8;
  }
  * { margin: 0; padding: 0; box-sizing: border-box; }
  html, body { width: 1200px; height: 900px; overflow: hidden; background: var(--stage); }
  .canvas { position: relative; width: 1200px; height: 900px; }

  .label {
    position: absolute; left: 290px; top: 50px; width: 620px; height: 800px;
    background: var(--orange); border-radius: 18px; overflow: hidden;
  }
  .label__pattern {
    position: absolute; inset: 0;
    background:
      radial-gradient(circle at 75% 14%, var(--orange-soft) 0 24%, transparent 25%),
      radial-gradient(circle at 95% 55%, var(--orange-soft) 0 20%, transparent 21%),
      radial-gradient(circle at 30% 6%, var(--orange-soft) 0 18%, transparent 19%),
      var(--orange);
  }
  .panel { position: absolute; left: 0; top: 0; width: 620px; height: 800px; }

  .brand {
    position: absolute; left: 245px; top: 140px;
    display: flex; align-items: center; gap: 8px;
    font-family: "Nunito Sans", sans-serif; font-weight: 800;
    font-size: 64px; color: var(--ink); letter-spacing: -1px; line-height: 1;
  }
  .brand__dot { width: 16px; height: 16px; border-radius: 50%; background: var(--orange); }

  .product-name {
    position: absolute; left: 232px; top: 222px; width: 240px;
    font-family: "Bebas Neue", sans-serif; font-weight: 400; font-size: 60px; line-height: 0.92;
    color: var(--ink); text-align: center;
  }
  .claim {
    position: absolute; left: 160px; top: 348px;
    font-family: "Oswald", sans-serif; font-weight: 300; font-size: 23px;
    line-height: 1.15; color: var(--ink); text-transform: uppercase;
  }
  .benefits {
    position: absolute; left: 300px; top: 418px; width: 250px; list-style: none;
    font-family: "Nunito Sans", sans-serif; font-weight: 600; font-size: 13px; color: var(--ink);
  }
  .benefits li { display: flex; align-items: center; gap: 8px; height: 29px; white-space: nowrap; }
  .benefits .num { font-family: "Oswald", sans-serif; font-weight: 300; font-size: 20px; width: 30px; }
  .benefits .num sub { font-size: 12px; }
  .benefits .icon { width: 22px; height: 14px; margin-right: 8px; border: 1.5px solid var(--ink); border-radius: 4px; flex: none; }

  .fruit-art {
    position: absolute; left: 160px; top: 450px; width: 128px; height: 110px;
    border-radius: 50px 50px 20px 20px;
    background: linear-gradient(180deg, #e6e6ea, #d5d5da);
  }
  .ingredients {
    position: absolute; left: 160px; top: 572px; width: 130px;
    font-family: "Nunito Sans", sans-serif; font-size: 7px; line-height: 1.35; color: var(--ink);
  }
  .flavour {
    position: absolute; left: 300px; top: 640px;
    font-family: "Bebas Neue", sans-serif; font-size: 24px; line-height: 1.2; color: #fff;
    background: var(--ink); border-radius: 6px; padding: 1px 10px;
  }
  .flavour-note {
    position: absolute; left: 302px; top: 676px;
    font-family: "Nunito Sans", sans-serif; font-style: italic; font-weight: 600;
    font-size: 9px; line-height: 1.25; color: var(--ink);
  }
  .mix-badge {
    position: absolute; left: 436px; top: 640px; width: 52px; height: 52px;
    border: 1.5px dashed var(--ink); border-radius: 50%;
    font-family: "Nunito Sans", sans-serif; font-weight: 800; font-size: 7.5px;
    display: flex; align-items: center; justify-content: center; text-align: center; line-height: 1.2; color: var(--ink);
  }
  .cert-badge {
    position: absolute; left: 498px; top: 634px; width: 38px; height: 62px;
    border: 2px solid var(--ink); border-radius: 5px;
  }
  .supplement {
    position: absolute; left: 300px; top: 710px;
    font-family: "Nunito Sans", sans-serif; font-style: italic; font-weight: 700; font-size: 16px; line-height: 1.4; color: var(--ink);
  }
  .supplement__weight { display: block; font-style: normal; font-weight: 400; }
</style>
</head>
<body>
<main class="canvas">
  <section class="label">
    <div class="label__pattern" role="img" aria-label="Repeating pattern of white concentric circles on orange"></div>

    <svg class="panel" viewBox="0 0 620 800" aria-hidden="true">
      <path d="M150 150 C150 110 190 110 230 110 L470 110 C540 110 555 180 555 250 L555 740 C530 760 520 800 500 800 L150 800 Z" fill="var(--panel)"/>
      <path d="M0 640 C40 600 90 560 110 470 C130 410 160 360 150 290 C140 240 130 200 100 180 C70 160 60 220 40 260 C20 300 0 320 0 350 Z" fill="var(--orange-deep)" opacity="0.75"/>
      <path d="M555 720 C590 710 610 730 620 750 L620 800 L520 800 C530 770 540 735 555 720 Z" fill="var(--orange)"/>
      <circle cx="532" cy="778" r="12" fill="var(--orange)"/>
    </svg>

    <div class="brand"><span class="brand__dot"></span>velmo</div>
    <h1 class="product-name">Collagen<br>Peptides</h1>
    <p class="claim">Ultimate complex for<br>joints flexibility &amp; mobility</p>

    <ul class="benefits">
      <li><span class="num">20<sub>g</sub></span>Collagen Peptides per Serving</li>
      <li><span class="icon"></span>Grass Fed + Pasture Raised</li>
      <li><span class="icon"></span>with turmeric added</li>
      <li><span class="icon"></span>Flexible joints, more mobility</li>
      <li><span class="icon"></span>Healthy inflammation response</li>
      <li><span class="icon"></span>Skin, hair, bones &amp; nails care</li>
      <li><span class="num">0<sub>g</sub></span>Sugar</li>
    </ul>

    <div class="fruit-art" role="img" aria-label="Line drawing of oranges and orange slices"></div>
    <p class="ingredients">ingredients<br>collagen, turmeric curcumin, vitamin c<br>Takes care of the joints mobility<br>and provides resilience against injuries</p>

    <span class="flavour">Orange</span>
    <p class="flavour-note">Naturally Flavored with<br>Other Natural Flavors</p>
    <div class="mix-badge">Just Add<br>8oz<br>Water</div>
    <div class="cert-badge"></div>
    <p class="supplement">Dietary Supplement<span class="supplement__weight">NET Wt. 10.6 Oz (300g)</span></p>
  </section>
</main>
</body>
</html>
```